Harbor Crestline (Business Card Design)

Need business cards designed. Something modern, chic, and sleek. Mabye the back of the card should be the navy blue that is in the logo and then just the logo on the back.

Target Market(s)

Those in the hotel, office, and renovation industry

Contact Information for Business Card

1. Logo 2. Tomasz Ferreiro 3. CEO/Founder 4. Phone: (833) HarbCre / (833) 427-2273 5. Email: tomasz@theharborcrestline.com 6. Website: www.theharborcrestline.com

Font styles to use
Other font styles liked:
• Look at the logo font and base the font for everything else off of that.

Colors
0054AA
0677BA
7BADD7
CADEEF
E8F1F8

Requirements
Must have
• Colors that are associated in the logo
Nice to have
• Sleek modern clean and chic design.

```html
<!DOCTYPE html>
<html lang="en">
<head>
<meta charset="utf-8">
<title>Harbor Crestline — Business Card</title>
<link rel="stylesheet" href="https://fonts.googleapis.com/css2?family=Montserrat:wght@500;600&display=swap">
<style>
  :root {
    --page: #ffffff;
    --navy: #0d1a40;
    --navy-faint: #1f2b52;
    --gold: #c9a13b;
    --white: #ffffff;
    --shadow: rgba(0, 0, 0, 0.45);
  }
  * { margin: 0; padding: 0; box-sizing: border-box; }
  html, body {
    width: 1200px; height: 1000px; overflow: hidden;
    background: var(--page);
    font-family: "Montserrat", sans-serif;
  }
  .canvas { position: relative; width: 1200px; height: 1000px; }

  .card {
    position: absolute;
    width: 620px; height: 353px;
    background: var(--navy);
    border-radius: 20px;
    overflow: hidden;
    box-shadow: 5px 6px 6px var(--shadow);
  }
  .card--front { left: 292px; top: 85px; }
  .card--back  { left: 290px; top: 562px; }

  /* brand lockup: plain square + name, one colour, one weight */
  .brand { position: absolute; display: flex; flex-direction: column; align-items: center; }
  .brand__square { width: 14px; height: 14px; background: var(--gold); margin-bottom: 18px; }
  .brand__name {
    color: var(--white); font-weight: 600; font-size: 30px;
    letter-spacing: 1.5px; line-height: 1.05; text-align: center;
  }
  .card--front .brand { left: 0; right: 0; top: 150px; }
  .card--back .brand { left: 372px; width: 214px; top: 164px; }
  .card--back .brand__name { font-size: 27px; }

  .front__backdrop {
    position: absolute; left: -30px; top: 252px;
    font-weight: 600; font-size: 66px; letter-spacing: 2px;
    color: var(--navy-faint); white-space: nowrap;
  }

  .back__title {
    position: absolute; left: 45px; top: 68px;
    color: var(--white); font-weight: 500; font-size: 22px; letter-spacing: 2.2px;
  }
  .back__role {
    position: absolute; left: 45px; top: 104px;
    color: var(--gold); font-weight: 600; font-size: 13px; letter-spacing: 4px;
  }
  .contacts { position: absolute; left: 44px; top: 166px; list-style: none; }
  .contact {
    display: flex; align-items: center; height: 20px; margin-bottom: 25px;
    font-size: 12.5px; font-weight: 500; letter-spacing: 1.3px; color: var(--white);
  }
  .contact svg { width: 20px; height: 20px; margin-right: 17px; flex: none; }
  .contact--phone { color: var(--gold); }
</style>
</head>
<body>
<main class="canvas">

  <section class="card card--front" aria-label="Card front">
    <div class="front__backdrop" aria-hidden="true">CRESTLINE</div>
    <div class="brand">
      <span class="brand__square"></span>
      <span class="brand__name">HARBOR<br>CRESTLINE</span>
    </div>
  </section>

  <section class="card card--back" aria-label="Card back">
    <h1 class="back__title">HARBOR CRESTLINE</h1>
    <p class="back__role">TOMASZ FERREIRO\CEO/FOUNDER</p>
    <ul class="contacts">
      <li class="contact contact--email">
        <svg viewBox="0 0 20 20" aria-hidden="true">
          <circle cx="10" cy="10" r="3.4" fill="none" stroke="var(--gold)" stroke-width="2"/>
          <path d="M13.4 7v4.2c0 1.6 2.8 1.8 3.2-.4A7 7 0 1 0 13.6 16" fill="none" stroke="var(--gold)" stroke-width="2" stroke-linecap="round"/>
        </svg>
        TOMASZ@THEHARBORCRESTLINE.COM
      </li>
      <li class="contact contact--phone">
        <svg viewBox="0 0 20 20" aria-hidden="true">
          <path d="M5 2.5l3 3.2-1.6 2.2c1 2.2 2.8 4 5 5l2.2-1.6 3.2 3-1.5 2.4C9 16.5 3.5 11 2.8 4z" fill="var(--white)"/>
        </svg>
        (833) HARBCRE / (833) 427-2273
      </li>
      <li class="contact contact--web">
        <svg viewBox="0 0 20 20" aria-hidden="true">
          <g fill="none" stroke="var(--gold)" stroke-width="1.6">
            <circle cx="10" cy="10" r="8"/>
            <ellipse cx="10" cy="10" rx="3.4" ry="8"/>
            <path d="M2 10h16M3.5 6h13M3.5 14h13"/>
          </g>
        </svg>
        WWW.THEHARBORCRESTLINE.COM
      </li>
    </ul>
    <div class="brand">
      <span class="brand__square"></span>
      <span class="brand__name">HARBOR<br>CRESTLINE</span>
    </div>
  </section>

</main>
</body>
</html>
```